Business Card Design and Logo Needed

I need Business Cards and a Logo for my website and public speaking business which can be found at: www.kelsa-thorn.example

I'm looking for creative and unique ideas. Some business cards I've found online that I like can be found at:
http://gigplatelo.example/general/18-smokin-hot-business-card-designs/

and at

http://www.vortaplume.example/2009/04/50-creative-business-cards-of-50-graphic-designers/

```html
<!DOCTYPE html>
<html lang="en">
<head>
<meta charset="utf-8">
<title>Kelsa Thorn — Business Card</title>
<link rel="stylesheet" href="https://fonts.googleapis.com/css2?family=Italianno&family=Oswald:wght@500&display=swap">
<style>
  :root {
    --page: #ffffff;
    --card: #2a0c0d;
    --card-deep: #220809;
    --sheen: #3d1a1b;
    --magenta: #d0237f;
    --magenta-soft: #8e1f57;
  }
  * { margin: 0; padding: 0; box-sizing: border-box; }
  html, body {
    width: 1200px; height: 900px; overflow: hidden;
    background: var(--page);
  }
  .canvas { position: relative; width: 1200px; height: 900px; }

  .card {
    position: absolute; left: 250px; width: 706px; height: 394px;
    border-radius: 44px; overflow: hidden;
    background: var(--card);
  }
  .card--front {
    top: 36px;
    background: linear-gradient(180deg,
      var(--card-deep) 0%, var(--card) 30%, var(--sheen) 46%,
      var(--card) 54%, var(--card-deep) 100%);
  }
  .card--back { top: 444px; background: var(--card-deep); }

  .ornament {
    position: absolute; left: 20px; top: 40px; width: 230px; height: 314px;
    border-radius: 40px;
    background: radial-gradient(ellipse at 50% 50%,
      rgba(208, 35, 127, 0.35) 0%, rgba(142, 31, 87, 0.18) 55%, rgba(42, 12, 13, 0) 100%);
    display: flex; align-items: center; justify-content: center;
  }
  .brand-mark {
    font-family: "Oswald", sans-serif; font-weight: 500;
    font-size: 26px; letter-spacing: 3px; text-transform: uppercase;
    color: var(--magenta);
  }

  .identity {
    position: absolute; left: 326px; top: 110px; width: 300px; text-align: center;
  }
  .identity__name {
    font-family: "Italianno", cursive; font-weight: 400;
    font-size: 62px; line-height: 1; color: var(--magenta);
    letter-spacing: 2px;
  }
  .identity__roles {
    margin-top: 6px;
    font-family: "Oswald", sans-serif; font-weight: 500;
    font-size: 10px; letter-spacing: 2px; color: var(--magenta);
  }

  .contact {
    position: absolute; left: 270px; top: 328px; width: 420px; text-align: center;
    font-family: "Oswald", sans-serif; font-weight: 500;
    font-size: 11px; letter-spacing: 1.5px; line-height: 18px;
    color: var(--magenta); text-transform: uppercase;
  }

  .tagline {
    position: absolute; left: 0; right: 0; top: 188px; text-align: center;
    font-family: "Oswald", sans-serif; font-weight: 500;
    font-size: 14px; letter-spacing: 5px; color: var(--magenta);
  }
</style>
</head>
<body>
<main class="canvas">
  <section class="card card--front" aria-label="Business card front">
    <div class="ornament" role="img" aria-label="Flourished swirl ornament around the monogram">
      <span class="brand-mark">Kelsa Thorn</span>
    </div>
    <div class="identity">
      <h1 class="identity__name">Kelsa Thorn</h1>
      <p class="identity__roles">SPEAKER, PHILANTHROPIST, AUTHOR</p>
    </div>
    <p class="contact">
      Phone: 0700055501 &nbsp;•&nbsp; E-mail: info@kelsa-thorn.example<br>
      www.kelsa-thorn.example
    </p>
  </section>

  <section class="card card--back" aria-label="Business card back">
    <p class="tagline">WONDER. EXPLORE. DREAM. ACHIEVE.</p>
  </section>
</main>
</body>
</html>
```